Brinevale Yacht Management Full Page Ad Flyer

Yacht Management Package also includes the following periodic Monthly services:

Monthly full vessel systems checklist inspections
Diver For Hull Cleaning And Inspection Of Props, Shafts, and Zincs
Interior/Exterior Detailing and scheduled washdowns
Manage Haulout
Pump-out Services
On-call Captain and Crew Services
Updates

Need more time to provide more content to designers and the printing press template file.

Target Market(s)

Vessel owners, motor yachts, sailboats from 25 feet in length up to 125 feet in length. We do not do cruise ships or yachts larger than 125 feet. Someone who has their boat docked at their house or a local marina. We also offer mobile on-site services.

```html
<!DOCTYPE html>
<html lang="en">
<head>
<meta charset="utf-8">
<title>Brinevale Yacht Management – Full Page Ad Flyer</title>
<link rel="stylesheet" href="https://fonts.googleapis.com/css2?family=Montserrat:wght@400;500;600&display=swap">
<style>
  :root {
    --backdrop: #e9ecec;
    --paper: #ffffff;
    --brand-slate: #2f4a6b;
    --panel-sage: #8d9f99;
    --ink: #1f1f1f;
    --white: #ffffff;
  }
  * { margin: 0; padding: 0; box-sizing: border-box; }
  html, body {
    width: 1200px; height: 1200px; overflow: hidden;
    background: var(--backdrop);
    font-family: "Montserrat", sans-serif;
  }
  .flyer {
    position: absolute; left: 234px; top: 83px;
    width: 731px; height: 1034px;
    background: var(--paper);
    overflow: hidden;
  }
  .hero-photo {
    position: absolute; left: 0; top: 0; width: 100%; height: 596px;
    background: linear-gradient(180deg, #93b3c4 0%, #b7ccd3 45%, #c9d6d6 62%, #4f8594 66%, #2f6577 100%);
  }
  .brand {
    position: absolute; left: 50px; top: 110px;
    width: 330px; text-align: center;
    color: var(--brand-slate); font-weight: 500;
  }
  .brand-name { font-size: 43px; letter-spacing: 7px; line-height: 1; }
  .brand-tag { font-size: 10px; letter-spacing: 7.5px; margin-top: 9px; }
  .services-panel {
    position: absolute; left: 94px; top: 550px;
    width: 544px; height: 155px;
    background: var(--panel-sage);
    display: flex; align-items: center; justify-content: center;
    padding: 0 24px;
  }
  .services-heading {
    color: var(--white); font-weight: 600;
    font-size: 26.5px; line-height: 1.26; text-align: center;
  }
  .service-list {
    position: absolute; left: 49px; top: 752px;
    list-style: none; color: var(--ink);
    font-size: 18px; line-height: 31px; font-weight: 400;
  }
  .service-list li { display: flex; align-items: center; }
  .service-list svg { width: 9px; height: 11px; margin-right: 7px; flex: none; }
</style>
</head>
<body>
  <main class="flyer">
    <div class="hero-photo" role="img" aria-label="Sport-fishing motor yacht cruising on open sea under a soft blue sky"></div>

    <div class="brand">
      <div class="brand-name">BRINEVALE</div>
      <div class="brand-tag">YACHT MANAGEMENT</div>
    </div>

    <div class="services-panel">
      <h1 class="services-heading">Yacht Management Package also includes the following periodic Monthly services:</h1>
    </div>

    <ul class="service-list">
      <li><svg viewBox="0 0 9 11"><path d="M1 1 L7 5.5 L1 10" fill="none" stroke="#1f1f1f" stroke-width="2.4"/></svg>Monthly full vessel systems checklist inspections</li>
      <li><svg viewBox="0 0 9 11"><path d="M1 1 L7 5.5 L1 10" fill="none" stroke="#1f1f1f" stroke-width="2.4"/></svg>Diver For Hull Cleaning And Inspection Of Props, Shafts, and Zincs</li>
      <li><svg viewBox="0 0 9 11"><path d="M1 1 L7 5.5 L1 10" fill="none" stroke="#1f1f1f" stroke-width="2.4"/></svg>Interior/Exterior Detailing and scheduled washdowns</li>
      <li><svg viewBox="0 0 9 11"><path d="M1 1 L7 5.5 L1 10" fill="none" stroke="#1f1f1f" stroke-width="2.4"/></svg>Manage Haulout</li>
      <li><svg viewBox="0 0 9 11"><path d="M1 1 L7 5.5 L1 10" fill="none" stroke="#1f1f1f" stroke-width="2.4"/></svg>Pump-out Services</li>
      <li><svg viewBox="0 0 9 11"><path d="M1 1 L7 5.5 L1 10" fill="none" stroke="#1f1f1f" stroke-width="2.4"/></svg>On-call Captain and Crew Services</li>
    </ul>
  </main>
</body>
</html>
```